Home page design for a live auction website.

Hi, we are looking at finding a good design for an auction website, only home page .. We will not be selling anything online, so the website will only be a portal where visitors can check about our company, upcoming auctions, online catalogues etc.
See attached our logo. Please use the same red that you see on the logo in the designs that you provide.
The final design should communicate high-end auction website, as we will be selling expensive piece of arts and antiques.
We should have a main frame where images of arts will circulate, with description of the art piece. just like on http://paris.vellmarotte-quisande.com/
(but with a better design overall) and of course a menu with different tabs, like "about us", "previous sales" "next sales", "contact" , "how to buy", "meet our specialists".

Target Market(s)

High end segment, who can afford to pay up to 250'000 for a piece of art

Industry/Entity Type

Online

Number of Pages Required

1 page

Requirements
Must have
• a frame with images rotating, just like on http://paris.vellmarotte-quisande.com/ . but the rest of the design should be more refined.
• we should also have a strong call to action, "Free online estimation", click here, estimation delivered in 48 hours"
Nice to have
• Tremaux Auctions, the brand should be well visible

```html
<!DOCTYPE html>
<html lang="en">
<head>
<meta charset="utf-8">
<title>Tremaux Auctions – Home</title>
<link href="https://fonts.googleapis.com/css2?family=Playfair+Display:wght@400;700&family=Open+Sans:wght@400;600;700&display=swap" rel="stylesheet">
<style>
:root{
  --red:#b3202a;
  --red-dark:#8f1820;
  --green:#3f9a3c;
  --ink:#2c363c;
  --slate:#36424a;
  --footer:#2a3338;
  --grey-bg:#eceeef;
  --text:#555d62;
  --muted:#8a9297;
  --white:#ffffff;
}
*{box-sizing:border-box;margin:0;padding:0}
html,body{width:861px;height:1200px;overflow:hidden}
body{font-family:"Open Sans",Arial,sans-serif;color:var(--text);background:var(--white);position:relative}

/* header */
.topbar{position:absolute;top:0;left:0;width:861px;height:34px;background:var(--white)}
.brand{position:absolute;left:70px;top:4px;width:130px;height:50px;background:var(--white);border:1px solid #e2e2e2;display:flex;align-items:center;justify-content:center;gap:6px;z-index:3}
.brand-mark{width:12px;height:12px;background:var(--red);flex:none}
.brand-name{font-family:"Playfair Display",Georgia,serif;font-weight:700;font-size:12px;color:var(--red);white-space:nowrap}
.phone{position:absolute;left:395px;top:10px;font-size:11px;color:var(--ink);display:flex;align-items:center;gap:5px}
.btn-est{position:absolute;left:545px;top:7px;height:20px;padding:0 14px;background:var(--green);color:#fff;font-size:11px;line-height:20px}
.flag{position:absolute;left:700px;top:11px;width:16px;height:11px;background:linear-gradient(#c8202a 0 50%,#fff 50%);border:1px solid #ccc}
.nav{position:absolute;top:34px;left:0;width:861px;height:23px;background:var(--red-dark)}
.nav ul{list-style:none;display:flex;position:absolute;left:225px;top:0;height:23px}
.nav li{color:#f3dcdc;font-size:10.5px;padding:0 14px;line-height:23px}
.nav li.active{background:var(--red);color:#fff}

/* hero */
.hero{position:absolute;top:57px;left:0;width:861px;height:303px;background:linear-gradient(120deg,#6a4a3a,#a07a5c 40%,#5a4a44 70%,#3a3230)}
.hero-caption{position:absolute;left:490px;top:153px;width:310px;height:100px;background:rgba(255,255,255,.95);padding:10px 16px}
.hero-caption h3{font-family:"Playfair Display",Georgia,serif;font-weight:400;font-size:13px;color:var(--ink);line-height:16px}
.hero-caption .price{position:absolute;left:16px;bottom:10px;color:var(--red);font-size:12px}
.hero-caption .arrows{position:absolute;right:14px;bottom:10px;display:flex;gap:10px}

/* estimation band */
.cta{position:absolute;top:360px;left:0;width:861px;height:55px;background:var(--slate)}
.cta-icon{position:absolute;left:256px;top:13px}
.cta h2{position:absolute;left:292px;top:10px;font-family:"Playfair Display",Georgia,serif;font-weight:400;font-size:19px;color:#fff;white-space:nowrap}
.cta p{position:absolute;left:292px;top:35px;font-size:9px;color:#c4cbcf;font-style:italic}
.cta .btn-click{position:absolute;left:525px;top:17px;height:22px;padding:0 18px;background:var(--green);color:#fff;font-size:10px;font-weight:700;line-height:22px}

/* highlight */
.highlight{position:absolute;top:415px;left:0;width:861px;height:260px;background:var(--white)}
.section-title{font-family:"Playfair Display",Georgia,serif;font-weight:400;font-size:24px;color:var(--ink);text-align:center;white-space:nowrap}
.highlight .section-title{position:absolute;top:32px;width:100%}
.title-rule{position:absolute;top:72px;left:380px;width:100px;height:1px;background:#ddd}
.hl-img{position:absolute;left:200px;top:100px;width:200px;height:130px;background:linear-gradient(135deg,#7a2e2a,#c8a880 50%,#6e5a4a)}
.hl-text{position:absolute;left:420px;top:100px;width:240px}
.hl-text .price{color:var(--red);font-size:13px;margin-bottom:8px}
.hl-text p{font-size:10.5px;line-height:15px;color:var(--muted)}
.hl-arrow{position:absolute;top:155px}

/* upcoming + news */
.lower{position:absolute;top:675px;left:0;width:861px;height:300px;background:var(--grey-bg)}
.lower .section-title{position:absolute;top:40px;text-align:left}
.up-title{left:70px}
.news-title{left:538px}
.up-nav{position:absolute;left:465px;top:50px;display:flex;gap:12px}
.card{position:absolute;top:95px;width:200px}
.card .img{height:120px}
.card p{background:#fff;font-size:9.5px;line-height:13px;padding:8px 10px;color:var(--ink);height:42px}
.news{position:absolute;left:548px;top:92px;width:210px;list-style:none}
.news li{border-bottom:1px solid #d6d9db;padding:5px 0 5px 18px;position:relative}
.news li::before{content:"";position:absolute;left:5px;top:10px;width:5px;height:5px;background:var(--red)}
.news b{display:block;font-weight:400;font-size:9px;color:var(--ink);line-height:12px}
.news span{font-size:7.5px;color:var(--muted);line-height:12px}

/* catalogue band */
.catalogue{position:absolute;top:975px;left:0;width:861px;height:60px;background:var(--red)}
.catalogue h2{position:absolute;left:200px;top:16px;font-family:"Playfair Display",Georgia,serif;font-weight:400;font-size:20px;color:#fff;white-space:nowrap}
.catalogue .btn-dl{position:absolute;left:560px;top:20px;height:20px;padding:0 16px;border:1px solid #fff;color:#fff;font-size:9px;line-height:18px;font-weight:600}

/* footer */
.footer{position:absolute;top:1035px;left:0;width:861px;height:165px;background:var(--footer);color:#aab3b8}
.col{position:absolute;top:20px}
.col h4{font-size:11px;color:#fff;font-weight:600;margin-bottom:8px}
.col p{font-size:9px;line-height:13px}
.col ul{list-style:none;font-size:9px;line-height:14px}
.about{left:40px;width:175px}
.links{left:255px;width:110px}
.signup{left:375px;width:190px}
.signup .field{height:18px;background:#fff;margin-top:8px}
.signup .btn-sub{margin-top:6px;height:18px;background:var(--green);color:#fff;font-size:9px;text-align:center;line-height:18px;font-weight:700}
.foot-brand{position:absolute;left:615px;top:40px;display:flex;align-items:center;gap:6px}
.foot-brand .brand-mark{background:#fff}
.foot-brand span{font-family:"Playfair Display",Georgia,serif;font-weight:700;font-size:13px;color:#fff}
.copy{position:absolute;left:615px;top:68px;font-size:8px;color:#7d878c}
</style>
</head>
<body>

<header class="topbar">
  <div class="brand"><span class="brand-mark"></span><span class="brand-name">Tremaux Auctions</span></div>
  <div class="phone">
    <svg width="10" height="10" viewBox="0 0 24 24"><path fill="#b3202a" d="M6.6 10.8a15 15 0 006.6 6.6l2.2-2.2c.3-.3.7-.4 1-.2 1.1.4 2.3.6 3.6.6.6 0 1 .4 1 1V20c0 .6-.4 1-1 1C10.6 21 3 13.4 3 4c0-.6.4-1 1-1h3.5c.6 0 1 .4 1 1 0 1.3.2 2.5.6 3.6.1.3 0 .7-.2 1z"/></svg>
    +1 (555) 014 2290
  </div>
  <div class="btn-est">Free Online Estimation</div>
  <div class="flag"></div>
</header>
<nav class="nav">
  <ul>
    <li>About Us</li><li class="active">Previous Sales</li><li>Next Sales</li><li>Contact Us</li><li>How to Buy</li><li>Meet Our Specialists</li>
  </ul>
</nav>

<section class="hero" role="img" aria-label="Photograph of collectors viewing artworks at a live auction preview">
  <div class="hero-caption">
    <h3>Karim El-Hadi ZAN (1901-1991)<br>Composition n° 29 Techniques<br>mixtes sur carton, signée</h3>
    <div class="price">45,000 €</div>
    <div class="arrows">
      <svg width="8" height="10" viewBox="0 0 8 10"><path d="M6 1L2 5l4 4" stroke="#2c363c" stroke-width="1.5" fill="none"/></svg>
      <svg width="8" height="10" viewBox="0 0 8 10"><path d="M2 1l4 4-4 4" stroke="#2c363c" stroke-width="1.5" fill="none"/></svg>
    </div>
  </div>
</section>

<section class="cta">
  <svg class="cta-icon" width="26" height="28" viewBox="0 0 26 28"><rect x="3" y="2" width="20" height="24" fill="none" stroke="#fff" stroke-width="2"/><path d="M8 9h10M8 14h10M8 19h6" stroke="#fff" stroke-width="2"/></svg>
  <h2>Free Online Estimation</h2>
  <p>Estimation Delivered in 48 Hours</p>
  <div class="btn-click">CLICK HERE</div>
</section>

<section class="highlight">
  <h2 class="section-title">Auction Highlight</h2>
  <div class="title-rule"></div>
  <svg class="hl-arrow" style="left:160px" width="10" height="16" viewBox="0 0 10 16"><path d="M8 2L2 8l6 6" stroke="#999" stroke-width="2" fill="none"/></svg>
  <div class="hl-img" role="img" aria-label="Photograph of the featured auction lot on display"></div>
  <div class="hl-text">
    <div class="price">8000 / 12000 €</div>
    <p>Lorem ipsum dolor sit amet, consectetur adipiscing elit, sed do eiusmod tempor incididunt labore. Ut dignissim magna veniam, quis nostrud exercitation ullamco laboris nisi aliquip commodo.</p>
  </div>
  <svg class="hl-arrow" style="left:695px" width="10" height="16" viewBox="0 0 10 16"><path d="M2 2l6 6-6 6" stroke="#999" stroke-width="2" fill="none"/></svg>
</section>

<section class="lower">
  <h2 class="section-title up-title">Upcoming Auctions</h2>
  <div class="up-nav">
    <svg width="8" height="12" viewBox="0 0 8 12"><path d="M6 1L2 6l4 5" stroke="#999" stroke-width="1.5" fill="none"/></svg>
    <svg width="8" height="12" viewBox="0 0 8 12"><path d="M2 1l4 5-4 5" stroke="#999" stroke-width="1.5" fill="none"/></svg>
  </div>
  <article class="card" style="left:70px">
    <div class="img" role="img" aria-label="Photograph of a carved rhinoceros horn cup" style="background:linear-gradient(135deg,#6a3418,#b4703a 55%,#e9dfd6)"></div>
    <p>Chinese Rhinoceros Horn Libation Cup, 17th/18th century</p>
  </article>
  <article class="card" style="left:285px">
    <div class="img" role="img" aria-label="Painted portrait of a court official in ceremonial robes" style="background:linear-gradient(160deg,#d9c7a8,#9a3a2a 55%,#3d3a4a)"></div>
    <p>Chinese Ancestor Portrait, Color Silk on Silk, 19th century</p>
  </article>
  <h2 class="section-title news-title">News</h2>
  <ul class="news">
    <li><b>Chinese Rhinoceros Horn Libation Cup, 17th/18th century</b><span>24 March 2024</span></li>
    <li><b>Chinese Rhinoceros Horn Libation Cup, 17th/18th century</b><span>18 March 2024</span></li>
    <li><b>Chinese Rhinoceros Horn Libation Cup, 17th/18th century</b><span>11 March 2024</span></li>
    <li><b>Chinese Rhinoceros Horn Libation Cup, 17th/18th century</b><span>02 March 2024</span></li>
  </ul>
</section>

<section class="catalogue">
  <h2>Download our online catalogues</h2>
  <div class="btn-dl">DOWNLOAD</div>
</section>

<footer class="footer">
  <div class="col about">
    <h4>About Company</h4>
    <p>Lorem ipsum dolor sit amet, consectetur adipiscing elit, sed do eiusmod tempor incididunt ut labore et dolore magna aliqua. Ut enim ad minim veniam, quis nostrud exercitation ullamco laboris nisi ut aliquip ex ea commodo consequat.</p>
  </div>
  <div class="col links">
    <h4>Quick links</h4>
    <ul><li>About Us</li><li>Previous Sales</li><li>Next Sales</li><li>Contact Us</li><li>How to Buy</li><li>Meet Our Specialists</li></ul>
  </div>
  <div class="col signup">
    <h4>Sign up for our newsletter</h4>
    <p>Receive auction news and catalogues first.</p>
    <div class="field"></div>
    <div class="btn-sub">SUBSCRIBE</div>
  </div>
  <div class="foot-brand"><span class="brand-mark"></span><span>Tremaux Auctions</span></div>
  <div class="copy">© 2024 Tremaux Auctions</div>
</footer>

</body>
</html>
```